CD Cover for collection of relaxation music called "Under Quiet Pines"

We'd like to design a CD cover for upload to Corvel Press on Request and to digital services like Zolvy. The template and size specs, photos, example font and text are attached. We need the song durations on the back cover as well and we expect to have those ready by Thursday. Other album and book covers are provided for use as thumbnails inside booklet next to titles. In addition to the finished images to the template specifications, we'd like a copy of the front cover and the back cover as square images to upload to digital services - 2500 dpi x 2500 dpi or larger in .png and .jpg formats. We will also need to add "For more information, visit GentleSoundHarbor.example" under the other available works list. Thanks and we look forward to working together.

Target Market(s)

Relaxation and meditation music. Yoga studios. Massage therapists. Reiki practitioners.

Industry/Entity Type

Music Download

Colors

Designer to choose colors to be used in the design.

Requirements
Must have
• Font consistent with previous works and a peaceful and attractive layout. Also, designers have discretion on which water images to use in which location. The goal is to have a cover image that stands out among other thumbnails in the stores and also for the images on the CD to tell a story of increasing peace and relaxation.

```html
<!DOCTYPE html>
<html lang="en">
<head>
<meta charset="utf-8">
<title>Under Quiet Pines – CD Cover and Disc</title>
<link rel="stylesheet" href="https://fonts.googleapis.com/css2?family=Cormorant+Garamond:ital,wght@1,500&family=Pinyon+Script&display=swap">
<style>
  :root {
    --page-bg: #e9e9e9;
    --teal-deep: #0f5e48;
    --teal-mid: #1f8a68;
    --teal-light: #3aa982;
    --sky: #2a9c8c;
    --glow: #c9f5dc;
    --ink-light: #f4faf6;
    --hub-grey: #cfcfcf;
    --hub-inner: #e6e6e6;
  }
  * { margin: 0; padding: 0; box-sizing: border-box; }
  html, body {
    width: 1200px; height: 849px; overflow: hidden;
    background: var(--page-bg);
  }
  .stage { position: relative; width: 1200px; height: 849px; }

  /* Front cover */
  .cover {
    position: absolute; left: 131px; top: 171px;
    width: 555px; height: 474px; overflow: hidden;
  }
  .cover-scene {
    position: absolute; inset: 0;
    background:
      radial-gradient(circle at 86% 12%, #d9ece4 0 5%, transparent 9%),
      linear-gradient(180deg, var(--sky) 0%, var(--teal-mid) 14%, var(--teal-deep) 26%, var(--teal-deep) 44%, #3f9f7c 45%, var(--teal-deep) 48%, #137054 62%, var(--teal-mid) 82%, #2f9270 100%);
  }
  .cover-frame { position: absolute; left: 0; top: 0; }
  .cover-title {
    position: absolute; left: 0; top: 0;
    font-family: "Pinyon Script", cursive;
    font-weight: 400;
    color: var(--ink-light);
    font-size: 68px; line-height: 1;
    text-shadow: 0 1px 3px rgba(0, 40, 30, .35);
  }
  .cover-title span { position: absolute; white-space: nowrap; }
  .cover-title .line-1 { left: 140px; top: 128px; }
  .cover-title .line-2 { left: 200px; top: 196px; }
  .cover-title .line-3 { left: 238px; top: 260px; }
  .cover-credits {
    position: absolute; left: 0; right: 0; top: 412px;
    text-align: center;
    font-family: "Cormorant Garamond", serif;
    font-style: italic; font-weight: 500;
    color: var(--ink-light);
    font-size: 21px; line-height: 23px;
    padding-right: 8px;
  }

  /* Disc label */
  .disc { position: absolute; left: 709px; top: 192px; }
  .disc-text {
    font-family: "Cormorant Garamond", serif;
    font-style: italic; font-weight: 500;
  }
  .disc-title { font-family: "Pinyon Script", cursive; }
</style>
</head>
<body>
<main class="stage">

  <section class="cover" aria-label="Front cover">
    <div class="cover-scene" role="img" aria-label="Moonlit lake at night with a pine treeline, a full moon, two swans on the water and faint angel wings, in teal green tones"></div>
    <svg class="cover-frame" width="555" height="474" viewBox="0 0 555 474" aria-hidden="true">
      <defs>
        <radialGradient id="ringGlow" cx="50%" cy="50%" r="50%">
          <stop offset="88%" stop-color="#9ee8c4" stop-opacity="0"/>
          <stop offset="95%" stop-color="#c9f5dc" stop-opacity=".85"/>
          <stop offset="100%" stop-color="#9ee8c4" stop-opacity="0"/>
        </radialGradient>
      </defs>
      <circle cx="274" cy="238" r="178" fill="url(#ringGlow)"/>
      <circle cx="274" cy="238" r="163" fill="none" stroke="#eafaf1" stroke-width="1.4" stroke-dasharray="1.5 3"/>
    </svg>
    <h1 class="cover-title">
      <span class="line-1">Under</span>
      <span class="line-2">Quiet</span>
      <span class="line-3">Pines</span>
    </h1>
    <p class="cover-credits">Healing Music for Body, Mind and Spirit<br>by Lena Marsh-Ardell</p>
  </section>

  <svg class="disc" width="466" height="466" viewBox="0 0 466 466" aria-label="Disc label">
    <defs>
      <linearGradient id="discScene" x1="0" y1="0" x2="0" y2="1">
        <stop offset="0" stop-color="#1f8a68"/>
        <stop offset=".2" stop-color="#0f5e48"/>
        <stop offset=".45" stop-color="#0f5e48"/>
        <stop offset=".47" stop-color="#3f9f7c"/>
        <stop offset=".5" stop-color="#0f5e48"/>
        <stop offset=".75" stop-color="#137054"/>
        <stop offset="1" stop-color="#2f9270"/>
      </linearGradient>
      <radialGradient id="discRim" cx="50%" cy="50%" r="50%">
        <stop offset="90%" stop-color="#9ee8c4" stop-opacity="0"/>
        <stop offset="96%" stop-color="#c9f5dc" stop-opacity=".8"/>
        <stop offset="100%" stop-color="#3aa982" stop-opacity=".9"/>
      </radialGradient>
    </defs>
    <circle cx="233" cy="233" r="232" fill="url(#discScene)" role="img" aria-label="Moonlit lake with two swans and faint angel wings in teal green"/>
    <circle cx="233" cy="233" r="232" fill="url(#discRim)"/>
    <circle cx="233" cy="233" r="211" fill="none" stroke="#eafaf1" stroke-width="1.3" stroke-dasharray="1.5 3"/>
    <text class="disc-title" x="233" y="150" text-anchor="middle" font-size="50" fill="var(--ink-light)">Under Quiet Pines</text>
    <text class="disc-text" x="233" y="330" text-anchor="middle" font-size="16.5" fill="var(--ink-light)">Healing Music for Body, Mind and Spirit</text>
    <text class="disc-text" x="233" y="350" text-anchor="middle" font-size="16.5" fill="var(--ink-light)">by Lena Marsh-Ardell</text>
    <g class="disc-hub">
      <circle cx="233" cy="233" r="69" fill="var(--hub-grey)"/>
      <circle cx="233" cy="233" r="69" fill="none" stroke="#0c4a39" stroke-width="1.5"/>
      <circle cx="233" cy="233" r="22" fill="var(--hub-inner)"/>
    </g>
  </svg>

</main>
</body>
</html>
```